Brindle Works Ltd

I'd like to create a company letterhead for the attached logo in word format.

I'd like to emphasis the icon in large translucent state from the left corner and ensure that the letterhead colouring matches the colour palette of the current logo with a contrast so it's clear to see. I've attached a copy of our sister company page on the app for reference.

```html
<!DOCTYPE html>
<html lang="en">
<head>
<meta charset="utf-8">
<title>Brindle Works Ltd – Letterhead</title>
<link href="https://fonts.googleapis.com/css2?family=Lato:wght@400;700&display=swap" rel="stylesheet">
<style>
  :root {
    --teal: #00b8a6;
    --teal-faint: #e3f6f3;
    --ink: #333333;
    --slate: #adadad;
    --paper: #ffffff;
    --backdrop: #8d8d8d;
  }
  * { margin: 0; padding: 0; box-sizing: border-box; }
  html, body {
    width: 1061px;
    height: 1200px;
    overflow: hidden;
    background: var(--backdrop);
    font-family: "Lato", sans-serif;
  }
  .letterhead {
    position: absolute;
    left: 120px;
    top: 20px;
    width: 820px;
    height: 1160px;
    background: var(--paper);
    overflow: hidden;
  }
  .letterhead__sheen {
    position: absolute;
    inset: 0;
    background:
      linear-gradient(165deg, rgba(0,0,0,0.025) 0%, rgba(0,0,0,0) 14%),
      linear-gradient(170deg, rgba(0,0,0,0) 40%, rgba(0,0,0,0.03) 41%, rgba(0,0,0,0) 62%);
  }
  .brand-disc {
    position: absolute;
    left: -93px;
    top: 573px;
    width: 522px;
    height: 522px;
    border-radius: 50%;
    background: var(--teal-faint);
  }
  .header {
    position: absolute;
    left: 61px;
    top: 66px;
    right: 40px;
    height: 64px;
    display: flex;
    align-items: center;
  }
  .brand {
    display: flex;
    align-items: center;
    gap: 10px;
    width: 259px;
  }
  .brand__dot {
    width: 18px;
    height: 18px;
    border-radius: 50%;
    background: var(--teal);
    flex: none;
  }
  .brand__name {
    font-size: 26px;
    font-weight: 400;
    color: var(--teal);
    white-space: nowrap;
  }
  .divider {
    width: 1px;
    height: 58px;
    background: var(--ink);
    opacity: 0.55;
  }
  .address {
    margin-left: 34px;
    width: 178px;
    font-size: 13.5px;
    line-height: 18px;
    color: var(--ink);
  }
  .address__company { color: var(--teal); font-weight: 700; }
  .contact {
    margin-left: 28px;
    list-style: none;
    font-size: 13.5px;
    line-height: 18px;
    color: var(--ink);
  }
  .contact__item { display: flex; align-items: center; gap: 7px; }
  .contact__icon { width: 12px; height: 12px; flex: none; }
  .footer {
    position: absolute;
    left: 0;
    bottom: 0;
    width: 820px;
    height: 58px;
  }
  .footer__band { position: absolute; inset: 0; }
  .footer__web {
    position: absolute;
    left: 0;
    width: 668px;
    top: 19px;
    text-align: center;
    font-size: 13px;
    letter-spacing: 4px;
    color: var(--paper);
  }
  .footer__web strong { font-weight: 700; }
</style>
</head>
<body>
  <main class="letterhead">
    <div class="letterhead__sheen"></div>
    <div class="brand-disc" aria-hidden="true"></div>

    <header class="header">
      <div class="brand">
        <span class="brand__dot"></span>
        <span class="brand__name">Brindle Works</span>
      </div>
      <span class="divider"></span>
      <address class="address" style="font-style:normal">
        <div class="address__company">Brindle Works Ltd</div>
        <div>48 Harrow Lane</div>
        <div>Milford, CT 06460</div>
      </address>
      <span class="divider"></span>
      <ul class="contact">
        <li class="contact__item">
          <svg class="contact__icon" viewBox="0 0 24 24" aria-label="Phone"><path fill="#00b8a6" d="M6.6 10.8c1.4 2.8 3.8 5.1 6.6 6.6l2.2-2.2c.3-.3.7-.4 1-.2 1.1.4 2.3.6 3.6.6.6 0 1 .4 1 1V20c0 .6-.4 1-1 1C10.6 21 3 13.4 3 4c0-.6.4-1 1-1h3.5c.6 0 1 .4 1 1 0 1.3.2 2.5.6 3.6.1.3 0 .7-.2 1z"/></svg>
          <span>(555) 014-2370</span>
        </li>
        <li class="contact__item">
          <svg class="contact__icon" viewBox="0 0 24 24" aria-label="Fax"><path fill="none" stroke="#00b8a6" stroke-width="2.4" d="M6 9V3h12v6M6 17H3V9h18v8h-3M6 14h12v7H6z"/></svg>
          <span>(555) 014-2370</span>
        </li>
        <li class="contact__item">
          <svg class="contact__icon" viewBox="0 0 24 24" aria-label="Email"><path fill="#00b8a6" d="M2 6h20v13H2z"/><path fill="none" stroke="#fff" stroke-width="2" d="M2 6l10 7 10-7"/></svg>
          <span>info@brindleworks.com</span>
        </li>
      </ul>
    </header>

    <footer class="footer">
      <svg class="footer__band" viewBox="0 0 820 58" preserveAspectRatio="none">
        <polygon fill="#00b8a6" points="0,0 653,0 617,58 0,58"/>
        <polygon fill="#adadad" points="662,0 820,0 820,58 628,58"/>
      </svg>
      <p class="footer__web">www.<strong>BrindleWorks</strong>.com</p>
    </footer>
  </main>
</body>
</html>
```